Canadian Christian Church needs design for new sermon series

A graphic design for our series and an invitation card to invite people to the series. Check design brief for more detailed information. Target audience: young families and young adults. Looking for a creative design that will get people's attention and create interest. See design brief for copy of design purchased for previous series.
entered Apr 4 incorrectly. Need a week to receive and review designs, and today is Apr 2/19. Thanks!
young families and young adults

```html
<!DOCTYPE html>
<html lang="en">
<head>
<meta charset="utf-8">
<title>Messy – Sermon Series Invitation</title>
<link href="https://fonts.googleapis.com/css2?family=Cinzel:wght@400;500&family=Roboto:wght@400;500;700&family=Roboto+Condensed:wght@400&display=swap" rel="stylesheet">
<style>
  :root {
    --purple: #8e2a8f;
    --ink: #1c1c1c;
    --paper: #fbfaf4;
    --paper-edge: #e4e1cc;
    --stage: #4b4b4b;
    --stage-dark: #333;
    --rule: #bdbdb4;
    --night: #0b0b0b;
    --white: #ffffff;
  }
  * { box-sizing: border-box; margin: 0; padding: 0; }
  html, body { width: 754px; height: 1200px; overflow: hidden; }
  body {
    background: radial-gradient(ellipse at 50% 50%, var(--stage) 0%, var(--stage-dark) 100%);
    font-family: "Roboto", Arial, sans-serif;
    color: var(--ink);
    position: relative;
  }
  .card {
    position: absolute;
    left: 69px;
    width: 617px;
    height: 484px;
    overflow: hidden;
    background: radial-gradient(ellipse at 55% 45%, var(--white) 0%, var(--paper) 45%, var(--paper-edge) 100%);
    box-shadow: 0 10px 18px rgba(0,0,0,.45);
  }
  .card--front { top: 95px; }
  .card--back { top: 630px; }

  .church-mark {
    position: absolute;
    display: flex;
    flex-direction: column;
    align-items: center;
    transform: translateX(-50%);
  }
  .church-mark__dot {
    width: 44px; height: 44px;
    border-radius: 50%;
    background: var(--purple);
  }
  .church-mark__name {
    margin-top: 6px;
    font-family: "Roboto Condensed", Arial, sans-serif;
    font-size: 12px;
    color: var(--ink);
    white-space: nowrap;
  }
  .card--front .church-mark { left: 447px; top: 21px; }
  .card--back .church-mark { left: 309px; top: 26px; }

  .artwork {
    position: absolute;
    left: 51px; top: 109px;
    width: 566px; height: 320px;
    background: radial-gradient(ellipse at 55% 55%, rgba(40,40,40,.55) 0%, rgba(110,110,110,.28) 40%, rgba(200,200,190,0) 75%);
  }
  .series-title {
    position: absolute;
    left: 279px; top: 90px;
    font-family: "Cinzel", Georgia, serif;
    font-size: 108px;
    font-weight: 400;
    line-height: 1;
    color: var(--purple);
    letter-spacing: -2px;
    white-space: nowrap;
    transform: scaleX(0.84);
    transform-origin: left top;
  }
  .series-tagline {
    position: absolute;
    left: 277px; top: 192px;
    font-family: "Cinzel", Georgia, serif;
    font-size: 21.5px;
    letter-spacing: .6px;
    color: var(--ink);
    white-space: nowrap;
  }
  .series-mission {
    position: absolute;
    left: 0; right: 0; top: 440px;
    text-align: center;
    font-family: "Cinzel", Georgia, serif;
    font-size: 18.5px;
    letter-spacing: .6px;
    color: var(--ink);
  }

  .service-intro {
    position: absolute; left: 0; right: 0; top: 94px;
    text-align: center;
    font-size: 21px;
    color: var(--ink);
  }
  .service-time {
    position: absolute; left: 0; right: 0; top: 113px;
    text-align: center;
    font-size: 38px;
    font-weight: 700;
    color: var(--purple);
    letter-spacing: .5px;
  }
  .panel-heading {
    position: absolute;
    font-size: 14px;
    font-weight: 500;
    color: var(--ink);
    padding-bottom: 6px;
    border-bottom: 1px solid var(--rule);
    white-space: nowrap;
  }
  .panel-heading em { font-style: normal; color: var(--purple); }
  .panel-heading--sermons { left: 51px; top: 170px; width: 224px; }
  .panel-heading--features { left: 358px; top: 170px; width: 194px; }

  .sermon-list {
    position: absolute; left: 51px; top: 201px;
    list-style: none;
    font-size: 13px;
    line-height: 16.8px;
  }
  .sermon-list li { display: flex; }
  .sermon-list .date { width: 81px; font-weight: 500; }

  .panel-divider {
    position: absolute; left: 326px; top: 170px;
    width: 1px; height: 172px;
    background: var(--rule);
  }
  .feature-list {
    position: absolute; left: 362px; top: 201px;
    list-style: none;
    font-size: 13px;
    line-height: 16.8px;
  }
  .feature-list li {
    position: relative;
    padding-left: 15px;
    margin-bottom: 6px;
    font-weight: 500;
  }
  .feature-list li::before {
    content: "";
    position: absolute; left: 0; top: 5px;
    width: 6px; height: 6px; border-radius: 50%;
    background: var(--ink);
  }

  .thicket {
    position: absolute; left: 0; right: 0; top: 352px; height: 60px;
    background: linear-gradient(to bottom, rgba(11,11,11,0) 0%, rgba(11,11,11,.7) 50%, var(--night) 100%);
  }
  .contact-band {
    position: absolute; left: 0; right: 0; top: 410px; bottom: 0;
    background: var(--night);
    color: var(--white);
    font-size: 13px;
  }
  .contact-item {
    position: absolute;
    display: flex; align-items: center; gap: 7px;
    white-space: nowrap;
  }
  .contact-item svg { width: 13px; height: 13px; fill: none; stroke: #cfcfcf; stroke-width: 1.4; }
  .contact-item--address { left: 0; right: 0; top: 22px; justify-content: center; }
  .contact-item--phone { left: 60px; top: 42px; }
  .contact-item--mail { left: 188px; top: 42px; }
  .contact-item--web { left: 407px; top: 42px; }
</style>
</head>
<body>

<section class="card card--front">
  <div class="church-mark">
    <span class="church-mark__dot"></span>
    <span class="church-mark__name">Maple Grove Family Church</span>
  </div>
  <div class="artwork" role="img" aria-label="Grungy ink illustration of a tangled hand reaching from a mess toward a white open hand beside a cross"></div>
  <h1 class="series-title">MESSY</h1>
  <p class="series-tagline">JOINING GOD IN THE MESS</p>
  <p class="series-mission">CONNECTING YOUNG FAMILIES TO CHRIST</p>
</section>

<section class="card card--back">
  <div class="church-mark">
    <span class="church-mark__dot"></span>
    <span class="church-mark__name">Maple Grove Family Church</span>
  </div>
  <p class="service-intro">The time of the services</p>
  <p class="service-time">SUNDAYS @ 10:30</p>

  <h2 class="panel-heading panel-heading--sermons"><em>Names &amp; Dates</em> of the sermons</h2>
  <ul class="sermon-list">
    <li><span class="date">April 28th:</span><span>“We Made This Mess”</span></li>
    <li><span class="date">May 5th:</span><span>“Bless in the Mess”</span></li>
    <li><span class="date">May 12th:</span><span>“Born into the Mess”</span></li>
    <li><span class="date">May 19th:</span><span>“Messy Work”</span></li>
    <li><span class="date">May 26th:</span><span>“Messy Church”</span></li>
    <li><span class="date">June 2nd:</span><span>“Messy Hospitality”</span></li>
    <li><span class="date">June 9th:</span><span>TBD</span></li>
    <li><span class="date">June 16th:</span><span>“Messy within Boundaries”</span></li>
  </ul>

  <div class="panel-divider"></div>

  <h2 class="panel-heading panel-heading--features"><em>Features</em> of the service</h2>
  <ul class="feature-list">
    <li>Staffed nursery &amp;<br>children’s program every Sunday</li>
    <li>Coffee &amp; snacks</li>
    <li>Everyone welcome</li>
  </ul>

  <div class="thicket" role="img" aria-label="Dark tangled thicket silhouette along the bottom edge"></div>
  <footer class="contact-band">
    <div class="contact-item contact-item--address">
      <svg viewBox="0 0 14 14"><path d="M7 13s-4-4.3-4-7.2a4 4 0 0 1 8 0C11 8.7 7 13 7 13z"/><circle cx="7" cy="5.8" r="1.4"/></svg>
      <span>Your Company Address Goes here</span>
    </div>
    <div class="contact-item contact-item--phone">
      <svg viewBox="0 0 14 14"><circle cx="7" cy="7" r="6"/><path d="M5 4.2l1 1.6-.7.8a4 4 0 0 0 2.1 2.1l.8-.7 1.6 1-.5 1.1c-2.6-.2-4.8-2.4-5-5z"/></svg>
      <span>+0123 456 789</span>
    </div>
    <div class="contact-item contact-item--mail">
      <svg viewBox="0 0 14 14"><rect x="1" y="3" width="12" height="8"/><path d="M1 3l6 5 6-5"/></svg>
      <span>info@yourcompanymailid.com</span>
    </div>
    <div class="contact-item contact-item--web">
      <svg viewBox="0 0 14 14"><circle cx="7" cy="7" r="6"/><ellipse cx="7" cy="7" rx="2.6" ry="6"/><path d="M1 7h12M2 4h10M2 10h10"/></svg>
      <span>www.yourwebsite.com</span>
    </div>
  </footer>
</section>

</body>
</html>
```